Dental Business Card Design w/logo

Classic, elegant w/a touch of contemporary
Upscale dental facility located in Modesto CA
Specializing in restorative & general dentistry
Providing exceptional customer service to the community
Updates

I prefer script and not bold writing
If you can use the phone; fax and email icons instead of spelling them out, it would be great
No bold colors
Classy and elegant
In the back of the card I would like to see something like this
Your Next Appointment:
Mon     Tue    Wed    Thur (a box next to each of them for marking)
Date:_______________ at_____________ AM    PM  (a box next to them for marking)

Thank you

Target Market(s)

Well established professional

Industry/Entity Type

Dental

Contact Information for Business Card

Lavinteya Morbundi DMD
4176 Larkspur Rd
Suite F7
Corvallen, CA 95418

Office: 209-731-5902
Fax: 209-731-8417
Email: morbundidmd@velmoranet.com

Requirements
Must have
• Unique classic logo
An easily repeatable design that can be used on letterhead and envelopes
Nice to have
• My initials incorporated into unique design
Should not have
• No cartoons or cheesy themes. This is a practice for the well established and professional individual.

```html
<!DOCTYPE html>
<html lang="en">
<head>
<meta charset="utf-8">
<title>Lavinteya Morbundi DMD – Business Card</title>
<link rel="stylesheet" href="https://fonts.googleapis.com/css2?family=Didact+Gothic&display=swap">
<style>
  :root {
    --card-bg: #040404;
    --text-light: #f1f2f2;
    --mark-grey: #c3cac7;
    --divider: #b9bebc;
  }
  html, body {
    margin: 0;
    padding: 0;
    width: 1200px;
    height: 702px;
    overflow: hidden;
    background: var(--card-bg);
  }
  .card {
    position: relative;
    width: 1200px;
    height: 702px;
    background: var(--card-bg);
    color: var(--text-light);
    font-family: "Didact Gothic", "Century Gothic", sans-serif;
  }
  .brand-mark {
    position: absolute;
    left: 40px;
    top: 205px;
    width: 300px;
    text-align: center;
    font-size: 50px;
    line-height: 1;
    color: var(--mark-grey);
    letter-spacing: 1px;
  }
  .practitioner {
    position: absolute;
    left: 40px;
    top: 462px;
    width: 300px;
    margin: 0;
    text-align: center;
    font-weight: 400;
    font-size: 38px;
    line-height: 56px;
    letter-spacing: 1px;
  }
  .practitioner span { display: block; }
  .divider {
    position: absolute;
    left: 366px;
    top: 44px;
    width: 3px;
    height: 614px;
    background: var(--divider);
  }
  .contact {
    position: absolute;
    left: 401px;
    top: 130px;
    margin: 0;
    font-style: normal;
    font-size: 40px;
    line-height: 55px;
    letter-spacing: 1.2px;
    word-spacing: 2px;
    white-space: nowrap;
  }
  .contact-row { margin: 0 0 55px; }
  .contact-row:last-child { margin-bottom: 0; }
  .contact-label {
    text-decoration: underline;
    text-underline-offset: 5px;
    text-decoration-thickness: 2px;
  }
</style>
</head>
<body>
  <main class="card">
    <div class="brand-mark">Morbundi</div>
    <h1 class="practitioner">
      <span>LAVINTEYA</span>
      <span>MORBUNDI</span>
      <span>DMD</span>
    </h1>
    <div class="divider"></div>
    <address class="contact">
      <p class="contact-row"><span class="contact-label">ADDRESS</span>: 4176 Larkspur Rd Suite F7<br>Corvallen, CA 95418</p>
      <p class="contact-row"><span class="contact-label">OFFICE</span>: 209-731-5902</p>
      <p class="contact-row"><span class="contact-label">FAX</span>: 209-731-8417</p>
      <p class="contact-row"><span class="contact-label">EMAIL</span>: morbundidmd@velmoranet.com</p>
    </address>
  </main>
</body>
</html>
```